Recipe Card Design

I have a small kitchen store in Livingston Montana, and I would like to have recipe cards (4x6 postcard) designed with my logo, lines for recipe writing, all in black and white. My website is here: www.brambleforkpantry.com

Store

```html
<!DOCTYPE html>
<html lang="en">
<head>
<meta charset="utf-8">
<title>Recipe Card – Bramble Fork Pantry</title>
<link rel="stylesheet" href="https://fonts.googleapis.com/css2?family=Cinzel:wght@700&family=Source+Sans+3:wght@400;600&display=swap">
<style>
  :root {
    --frame: #000000;
    --card: #ffffff;
    --ink: #111111;
    --rule: #222222;
    --muted: #5b6466;
    --sketch: #e4e4e4;
    --sketch-edge: #cfcfcf;
  }
  * { margin: 0; padding: 0; box-sizing: border-box; }
  html, body { width: 1200px; height: 930px; overflow: hidden; background: var(--frame); }
  .canvas { position: relative; width: 1200px; height: 930px; background: var(--frame); font-family: "Source Sans 3", "Myriad Pro", sans-serif; color: var(--ink); }
  .card { position: absolute; left: 30px; top: 28px; width: 1140px; height: 872px; background: var(--card); border-radius: 40px; }
  .abs { position: absolute; }

  .brand-mark { left: 88px; top: 65px; width: 250px; height: 320px; display: flex; align-items: center; justify-content: center; gap: 10px; }
  .brand-mark .square { width: 18px; height: 18px; background: var(--ink); flex: none; }
  .brand-mark .name { font-weight: 600; font-size: 42px; line-height: 1.05; letter-spacing: 1px; text-transform: uppercase; }

  .recipe-label { left: 425px; top: 92px; font-size: 32px; font-variant: small-caps; letter-spacing: .5px; }
  .from-line { left: 425px; top: 136px; font-size: 29px; }
  .shop-title { left: 425px; top: 178px; font-family: "Cinzel", "Copperplate", serif; font-weight: 700; font-size: 29px; letter-spacing: .3px; }
  .meta { top: 255px; font-size: 26px; }
  .rule { position: absolute; height: 0; border-top: 1.6px solid var(--rule); }

  .sketch { background: linear-gradient(180deg, var(--sketch), var(--sketch-edge)); border-radius: 18px; }

  .section-label { font-size: 25px; text-transform: uppercase; }
  .divider { left: 489px; top: 410px; width: 0; height: 358px; border-left: 2.5px solid var(--rule); }

  .contact { left: 258px; top: 796px; font-size: 23px; line-height: 30px; color: var(--muted); }
  .contact svg { width: 20px; height: 20px; vertical-align: -3px; margin-right: 4px; }
  .web { left: 588px; top: 856px; font-size: 23px; color: var(--muted); }
</style>
</head>
<body>
<div class="canvas">
  <div class="card"></div>

  <div class="abs brand-mark">
    <span class="square"></span>
    <span class="name">Bramble<br>Fork<br>Pantry</span>
  </div>

  <div class="abs recipe-label">Recipe:</div>
  <div class="rule" style="left:540px;top:126px;width:572px"></div>
  <div class="abs from-line">From the Kitchen of</div>
  <div class="abs shop-title">BRAMBLE FORK PANTRY</div>

  <div class="abs meta" style="left:423px">Serves</div>
  <div class="rule" style="left:515px;top:285px;width:105px"></div>
  <div class="abs meta" style="left:633px">Cook Time</div>
  <div class="rule" style="left:776px;top:285px;width:104px"></div>
  <div class="abs meta" style="left:899px">Oven Time</div>
  <div class="rule" style="left:1044px;top:285px;width:104px"></div>

  <div class="abs sketch" role="img" aria-label="Line sketch of bread rolls and a round loaf" style="left:555px;top:305px;width:150px;height:72px"></div>
  <div class="abs sketch" role="img" aria-label="Line sketch of a woven basket filled with bread and herbs" style="left:738px;top:300px;width:168px;height:128px"></div>
  <div class="abs sketch" role="img" aria-label="Line sketch of wheat stalks" style="left:928px;top:297px;width:158px;height:123px"></div>

  <div class="abs section-label" style="left:75px;top:418px">Ingredients:</div>
  <div class="rule" style="left:75px;top:480px;width:372px"></div>
  <div class="rule" style="left:75px;top:515px;width:372px"></div>
  <div class="rule" style="left:75px;top:548px;width:372px"></div>
  <div class="rule" style="left:75px;top:584px;width:372px"></div>
  <div class="rule" style="left:75px;top:618px;width:372px"></div>
  <div class="rule" style="left:75px;top:655px;width:372px"></div>
  <div class="rule" style="left:75px;top:690px;width:372px"></div>
  <div class="rule" style="left:75px;top:725px;width:372px"></div>
  <div class="rule" style="left:75px;top:765px;width:372px"></div>

  <div class="abs divider"></div>

  <div class="abs section-label" style="left:541px;top:410px">Directions:</div>
  <div class="rule" style="left:541px;top:472px;width:597px"></div>
  <div class="rule" style="left:541px;top:507px;width:597px"></div>
  <div class="rule" style="left:541px;top:544px;width:597px"></div>
  <div class="rule" style="left:541px;top:578px;width:597px"></div>
  <div class="rule" style="left:541px;top:612px;width:597px"></div>
  <div class="rule" style="left:541px;top:648px;width:597px"></div>
  <div class="rule" style="left:541px;top:685px;width:597px"></div>
  <div class="rule" style="left:541px;top:720px;width:597px"></div>
  <div class="rule" style="left:541px;top:760px;width:597px"></div>

  <div class="abs contact">
    218 West Park Street<br>
    Willow Bend, MT 59012<br>
    <svg viewBox="0 0 20 20" aria-hidden="true"><circle cx="10" cy="10" r="9" fill="none" stroke="currentColor" stroke-width="1.4"/><path d="M7 5.5c-1 1-1 3 .5 5.5s3.5 4 5 4l1-1.3-2-1.6-1 .8c-.9-.5-2-1.8-2.4-2.8l.9-.9-1.2-2.3z" fill="currentColor"/></svg>(406) 555.0148
  </div>
  <div class="abs web">www.brambleforkpantry.com</div>
</div>
</body>
</html>
```